Tidal Hounds Dog Behaviour, Training and Natural Healthcare Business Card Design

I am an experienced and qualified dog behavioural trainer and natural animal healthcare consultant offering a range of services to help pet dog owners with the "whole dog".
COLOURS: A soft light blue in the background - can be fading out or split, red should also feature
LOGO: Dog, healing hands, silhouette, shadow
SERVICES: Behaviour Consults, Training, Complex Skills Coaching Walking Coaching, Diet & Nutrition, Environmental Enrichment, Lifestyle and Lifestage Adaptations, Massage, Natural Health Options
BY LINE: Happy Dogs, Happy Owners
VALUES: Promoting communication and connection between dogs and their owners.
FOCUS: Nutritional guidance and environmental adaptation are often needed to complete the package and increase the success rate of training and behaviour modification.

Target Market(s)

Everyone who has a dog who they wish to improve their relationship with

Industry/Entity Type

Communication

Contact Information for Business Card

Tidal Hounds, Rosalind Vukovic, 0417 286350, tidalhounds7@quellmail.net, www.tidalhounds7.net, Qualified Dog Behavioural Trainer and Natural Animal Healthcare Consultant

Font styles to use
Sans Serif
Script

Colors
85cae6
ec2027

Requirements
Must have
• A clear indication that it is a dog services business. A raised feature
Should not have
• Pawprints, cartoons

Files

```html
<!DOCTYPE html>
<html lang="en">
<head>
<meta charset="utf-8">
<title>Tidal Hounds Business Card</title>
<link rel="stylesheet" href="https://fonts.googleapis.com/css2?family=Montserrat:wght@700&family=Open+Sans:wght@400&family=Tinos&display=swap">
<style>
  :root {
    --red: #ec2027;
    --red-deep: #c81d25;
    --blue: #85cae6;
    --blue-strong: #1e9bd7;
    --blue-light: #a6dcf3;
    --white: #ffffff;
    --ink: #1a1a1a;
    --page: #e6e6e6;
  }
  * { margin: 0; padding: 0; box-sizing: border-box; }
  html, body {
    width: 1200px; height: 898px; overflow: hidden;
    background: var(--page);
  }
  .card {
    position: absolute; left: 100px; top: 163px;
    width: 1000px; height: 572px;
    background: var(--white);
    box-shadow: 0 10px 30px rgba(0,0,0,0.25);
    overflow: hidden;
  }
  .card-bands { position: absolute; inset: 0; }
  .brand {
    position: absolute; left: 60px; top: 120px;
    display: flex; align-items: center; gap: 14px;
    font-family: "Montserrat", sans-serif; font-weight: 700;
    font-size: 44px; color: var(--red); letter-spacing: 0.5px;
  }
  .brand-dot {
    width: 38px; height: 38px; border-radius: 50%;
    background: var(--red);
  }
  .holder {
    position: absolute; right: 70px; top: 62px; text-align: right;
  }
  .holder-name {
    font-family: "Montserrat", sans-serif; font-weight: 700;
    font-size: 38px; color: var(--red);
    padding-bottom: 6px;
    border-bottom: 2px solid var(--blue-strong);
    display: inline-block;
  }
  .holder-title {
    font-family: "Tinos", serif; font-size: 19px; color: var(--ink);
    line-height: 1.2; margin-top: 6px;
  }
  .dog-figure {
    position: absolute; left: 70px; top: 240px; width: 360px; height: 300px;
    border-radius: 40% 45% 20% 30%;
    background: radial-gradient(ellipse at 50% 40%, rgba(255,255,255,0.35), rgba(255,255,255,0.05) 70%, rgba(255,255,255,0));
  }
  .contact {
    position: absolute; left: 600px; top: 270px;
    list-style: none;
    font-family: "Open Sans", sans-serif; font-size: 22px; color: var(--white);
  }
  .contact-item { display: flex; align-items: center; gap: 10px; height: 40px; }
  .contact-icon { width: 24px; height: 24px; flex: none; }
</style>
</head>
<body>
  <div class="card">
    <svg class="card-bands" width="1000" height="572" viewBox="0 0 1000 572" aria-hidden="true">
      <defs>
        <radialGradient id="blueField" cx="0.45" cy="0.55" r="0.7">
          <stop offset="0" stop-color="#a6dcf3"/>
          <stop offset="0.6" stop-color="#3fb0e4"/>
          <stop offset="1" stop-color="#1e9bd7"/>
        </radialGradient>
      </defs>
      <rect x="0" y="0" width="1000" height="26" fill="var(--red-deep)"/>
      <polygon points="0,240 790,240 790,190 1000,190 1000,430 0,430" fill="url(#blueField)"/>
      <polygon points="770,190 805,190 790,212" fill="var(--white)"/>
      <rect x="0" y="430" width="1000" height="142" fill="var(--red)"/>
      <rect x="0" y="540" width="1000" height="32" fill="var(--red-deep)"/>
    </svg>

    <div class="brand"><span class="brand-dot"></span>Tidal Hounds</div>

    <div class="holder">
      <div class="holder-name">Rosalind Vukovic</div>
      <div class="holder-title">Dog Behavioural Trainer and<br>Natural Animal Healthcare Consultant</div>
    </div>

    <div class="dog-figure" role="img" aria-label="White line drawing of a standing dog in profile"></div>

    <ul class="contact">
      <li class="contact-item">
        <svg class="contact-icon" viewBox="0 0 24 24" aria-hidden="true"><rect width="24" height="24" rx="5" fill="#fff"/><path d="M8 6l2 3-1.5 1.5a8 8 0 0 0 5 5L15 14l3 2-1 2.5C11 18 6 13 5.5 7z" fill="var(--blue-strong)"/></svg>
        0417 286350
      </li>
      <li class="contact-item">
        <svg class="contact-icon" viewBox="0 0 24 24" aria-hidden="true"><rect width="24" height="24" rx="5" fill="#fff"/><rect x="5" y="7" width="14" height="10" fill="none" stroke="var(--blue-strong)" stroke-width="1.6"/><path d="M5 7l7 6 7-6" fill="none" stroke="var(--blue-strong)" stroke-width="1.6"/></svg>
        tidalhounds7@quellmail.net
      </li>
      <li class="contact-item">
        <svg class="contact-icon" viewBox="0 0 24 24" aria-hidden="true"><rect width="24" height="24" rx="5" fill="#fff"/><circle cx="12" cy="12" r="6.5" fill="none" stroke="var(--blue-strong)" stroke-width="1.5"/><path d="M5.5 12h13M12 5.5c-3 3.5-3 9.5 0 13M12 5.5c3 3.5 3 9.5 0 13" fill="none" stroke="var(--blue-strong)" stroke-width="1.2"/></svg>
        www.tidalhounds7.net
      </li>
    </ul>
  </div>
</body>
</html>
```